Brambury Logistics

Create a modern, simple, Elegant business card design for my business.

Services: Tamo Trucks, Transport, Contract Logistics,

Industry/Entity Type

Business

Contact Information for Business Card

Include all details same as old card plus new website address: www.bramburylogistics.com.au

Requirements
Must have
• Similar colors to Logo.

```html
<!DOCTYPE html>
<html lang="en">
<head>
<meta charset="utf-8">
<title>Brambury Logistics – Business Card</title>
<link href="https://fonts.googleapis.com/css2?family=Roboto:wght@300;400;500;700&display=swap" rel="stylesheet">
<style>
  :root{
    --page:#ecebe8;
    --card:#fbfbfb;
    --blue:#1673b3;
    --blue-light:#1fa3d6;
    --grey:#6d6f72;
    --text:#3a3c3f;
    --band:#dfe6e3;
    --white:#ffffff;
  }
  *{margin:0;padding:0;box-sizing:border-box}
  html,body{width:1200px;height:1023px;overflow:hidden}
  body{background:var(--page);font-family:"Roboto",sans-serif;position:relative}
  .card{position:absolute;width:640px;height:390px;border-radius:18px;overflow:hidden;
        box-shadow:0 10px 28px rgba(0,0,0,.18)}
  /* front */
  .card-front{left:70px;top:70px;background:linear-gradient(160deg,#ffffff 0%,#f1f2f3 100%)}
  .card-front .swoosh{position:absolute;inset:0}
  .brand{position:absolute;left:48px;top:62px;display:flex;align-items:center;gap:14px}
  .brand-mark{width:22px;height:22px;background:var(--blue)}
  .brand-name{font-size:38px;font-weight:700;color:var(--blue);letter-spacing:.5px}
  .contact{position:absolute;left:48px;top:228px;color:var(--text)}
  .contact .name{font-size:28px;font-weight:500;color:var(--blue);line-height:1}
  .contact .title{font-size:15px;font-weight:400;margin:4px 0 14px;color:var(--grey)}
  .contact ul{list-style:none}
  .contact li{display:flex;align-items:center;gap:10px;font-size:16px;font-weight:300;line-height:26px}
  .contact svg{width:14px;height:14px;flex:none}
  .website{position:absolute;right:30px;bottom:26px;font-size:16px;font-weight:300;color:var(--text);letter-spacing:.6px}
  /* back */
  .card-back{left:490px;top:563px}
  .back-photo{position:absolute;inset:0;
    background:linear-gradient(115deg,#6f8d57 0%,#88a56a 28%,#9fb3a4 48%,#5f7780 72%,#364650 100%)}
  .back-band{position:absolute;left:-60px;top:86px;width:820px;height:46px;background:var(--band);
    opacity:.92;transform:rotate(28deg);transform-origin:left top;display:flex;align-items:center;padding-left:120px}
  .services{font-size:17px;font-weight:500;color:var(--blue);letter-spacing:.6px;white-space:nowrap}
  .back-brand{position:absolute;right:44px;top:150px;display:flex;align-items:center;gap:14px}
  .back-brand .brand-mark{background:var(--white)}
  .back-brand .brand-name{color:var(--white);font-size:40px}
</style>
</head>
<body>
  <section class="card card-front">
    <svg class="swoosh" viewBox="0 0 640 390" preserveAspectRatio="none">
      <path d="M330 390 C380 250 470 110 640 40 L640 52 C490 120 400 260 360 390 Z" fill="var(--blue)"/>
      <path d="M330 390 C352 320 380 270 410 230 C388 280 372 330 360 390 Z" fill="var(--blue-light)"/>
    </svg>
    <div class="brand">
      <span class="brand-mark"></span>
      <span class="brand-name">Brambury Logistics</span>
    </div>
    <div class="contact">
      <p class="name">Your Name</p>
      <p class="title">Title</p>
      <ul>
        <li><svg viewBox="0 0 14 14"><circle cx="7" cy="7" r="6" fill="none" stroke="#3a3c3f"/><path d="M5 4.5l1 1.5-.6.6a4 4 0 002 2l.6-.6 1.5 1-.6 1C6.5 10 4 7.5 4 5.1z" fill="#3a3c3f"/></svg>0400 555 019</li>
        <li><svg viewBox="0 0 14 14"><rect x="1" y="3" width="12" height="8" fill="none" stroke="#3a3c3f"/><path d="M1 3l6 5 6-5" fill="none" stroke="#3a3c3f"/></svg>Reece@bramburylogistics.com.au</li>
        <li><svg viewBox="0 0 14 14"><circle cx="7" cy="7" r="6" fill="none" stroke="#3a3c3f"/><circle cx="7" cy="7" r="2.2" fill="#3a3c3f"/></svg>Western Australia</li>
      </ul>
    </div>
    <p class="website">www.bramburylogistics.com.au</p>
  </section>

  <section class="card card-back">
    <div class="back-photo" role="img" aria-label="Photo of an open country road through green fields under a cloudy sky"></div>
    <div class="back-band"><span class="services">Tamo Trucks &nbsp;|&nbsp; Transport &nbsp;|&nbsp; Contract Logistics</span></div>
    <div class="back-brand">
      <span class="brand-mark"></span>
      <span class="brand-name">Brambury Logistics</span>
    </div>
  </section>
</body>
</html>
```